design a web site for equipment and software pos company

We would a web site similar to the site we whited labed our rbts system .https://tryvelko.com/
website would be on RbTillSystems.com
we would a contact page
877-555-0148

We do not want an exact copy just something similar .
we are tablet po system

we are at

we are selling hardware and software

rb till systems
41 cedar hollow ln
warren, nj 07059
we are cloud based system

Target Market(s)

any retail merchant

Industry/Entity Type

credit card processing in POS asystems

Coding

Coded - Design and coding required

Number of Pages Required

5+ page

Requirements
Must have
• be able to connect webnarra hosting
Nice to have
• modern looking site
Should not have
• any red

```html
<!DOCTYPE html>
<html lang="en">
<head>
<meta charset="utf-8">
<title>RB Till Systems — White Label</title>
<link href="https://fonts.googleapis.com/css2?family=Bellefair&family=Nunito+Sans:wght@400;600;700;800;900&display=swap" rel="stylesheet">
<style>
:root{
  --ink:#1d1d1f;
  --dark:#0d0d0d;
  --blue:#1f4e86;
  --yellow:#f0c419;
  --grey-bg:#f6f6f6;
  --sky:#e3f2fb;
  --white:#ffffff;
  --rule:#d9e3ea;
}
*{margin:0;padding:0;box-sizing:border-box}
html,body{width:691px;height:1200px;overflow:hidden}
body{position:relative;background:var(--white);font-family:"Nunito Sans",sans-serif;color:var(--ink)}
.abs{position:absolute}
.display{font-family:"Bellefair",serif;font-weight:400;color:var(--ink)}

/* hero */
.hero{left:0;top:0;width:691px;height:282px;clip-path:polygon(0 0,100% 0,100% 216px,0 282px);
  background:linear-gradient(100deg,#050505 0%,#151210 38%,#3b2c1f 62%,#8a6340 80%,#4a3828 100%)}
.brand{left:42px;top:10px;color:var(--white);font-size:13px;font-weight:700;display:flex;align-items:center;gap:5px}
.brand .mark{width:12px;height:12px;border-radius:50%;background:var(--yellow)}
.nav{top:20px;font-size:8px;font-weight:700;color:var(--white)}
.nav.active{color:var(--yellow)}
.hero-kicker{left:40px;top:128px;font-size:27px;color:var(--white)}
.hero-title{left:40px;top:160px;font-size:31px;font-weight:900;color:var(--white);letter-spacing:.3px}

/* benefits */
.section-title{left:0;width:691px;text-align:center;font-size:26px}
.benefit{width:196px;text-align:center}
.benefit svg{display:block;margin:0 auto}
.benefit h3{margin-top:17px;font-size:11px;font-weight:700;color:var(--blue);line-height:16px}
.benefit p{margin-top:10px;font-size:8.6px;line-height:14.3px}

/* organic */
.band-grey{left:0;top:536px;width:691px;height:664px;background:var(--grey-bg)}
.band-sky{left:0;top:714px;width:691px;height:486px;background:var(--sky);clip-path:polygon(0 124px,100% 0,100% 100%,0 100%)}
.photo{left:42px;top:579px;width:223px;height:153px;border:2px solid var(--white);box-shadow:0 1px 4px rgba(0,0,0,.25);
  background:radial-gradient(ellipse at 45% 50%,#8a5a33 0%,#6b4426 60%,#4e311c 100%)}
.organic-title{left:302px;top:584px;font-size:26px;line-height:33px}
.organic-copy{left:299px;top:660px;width:352px;font-size:8.6px;line-height:14.3px}

/* grow */
.hand-disc{left:42px;top:872px;width:90px;height:90px;border-radius:50%;background:var(--white);box-shadow:0 0 6px rgba(0,0,0,.12)}
.hand-disc span{position:absolute;left:15px;top:20px;width:60px;height:50px;border-radius:22px;background:linear-gradient(135deg,#f8b4a8,#fbd7c9 60%,#9fd3ea)}
.grow-title{left:144px;top:884px;font-size:26px}
.grow-copy{left:145px;top:920px;width:310px;font-size:8.6px;line-height:14.3px}
.mail{left:507px;top:891px;width:142px;height:26px;border:1px solid #b9c3ca;background:var(--white);font-size:7.6px;text-align:center;line-height:24px}
.subscribe{left:507px;top:920px;width:142px;height:26px;background:var(--yellow);font-size:7.6px;font-weight:800;text-align:center;line-height:26px;letter-spacing:.3px}

/* footer */
.foot-head{top:993px;font-family:"Bellefair",serif;font-size:10.5px}
.foot-rule{left:40px;top:1014px;width:606px;height:1px;background:var(--rule)}
.foot-sep{top:1014px;width:1px;height:101px;background:var(--rule)}
.foot-sep i{position:absolute;left:0;top:13px;width:1px;height:17px;background:var(--yellow)}
.foot-list{top:1025px;list-style:none;font-size:7.6px;line-height:16px}
.contact-row{left:507px;font-size:7.6px;line-height:12px;display:flex;gap:9px;align-items:flex-start}
.contact-row svg{flex:none;margin-top:2px}
.follow{left:507px;top:1116px;font-size:7.6px}
.social{top:1111px;width:21px;height:21px;border:1px solid #2a2a2a;border-radius:50%}
.copyright{left:0;top:1161px;width:691px;text-align:center;font-size:7.6px}
</style>
</head>
<body>

<div class="abs hero" role="img" aria-label="Photo of a tablet point of sale terminal with card reader and receipt printer on a wooden counter"></div>
<div class="abs brand"><span class="mark"></span>RB Till Systems</div>
<nav>
  <span class="abs nav" style="left:405px">Features</span>
  <span class="abs nav" style="left:453px">About</span>
  <span class="abs nav" style="left:490px">Business Types</span>
  <span class="abs nav" style="left:560px">Products</span>
  <span class="abs nav active" style="left:609px">White lebel</span>
</nav>
<div class="abs display hero-kicker">White Label</div>
<h1 class="abs hero-title">GROWTH EXCELLENCE</h1>

<h2 class="abs display section-title" style="top:296px">Benefits of a White Label POS</h2>

<div class="abs benefit" style="left:41px;top:364px">
  <svg width="38" height="38" viewBox="0 0 38 38" fill="none" stroke="#111" stroke-width="1.3">
    <path d="M2 36h34M5 36V26h5v10M13 36V22h5v14M21 36V18h5v14M29 36V12h5v24"/>
    <path d="M3 20C14 17 24 10 34 2M28 2h6v6"/>
  </svg>
  <h3>Leading POS Software &amp;<br>Secure Partner Portal</h3>
  <p>It is a long established fact that a reader will be distracted by the readable content of a page when looking at its layout.</p>
</div>
<div class="abs benefit" style="left:247px;top:364px">
  <svg width="40" height="38" viewBox="0 0 40 38" fill="none" stroke="#111" stroke-width="1.3">
    <circle cx="14" cy="11" r="6"/><circle cx="14" cy="11" r="2.5"/>
    <path d="M14 3v2M14 17v2M6 11h2M20 11h2M24 5h8M24 11h8M24 17h8M32 5v12"/>
    <circle cx="36" cy="5" r="2"/><circle cx="36" cy="17" r="2"/>
    <path d="M2 30l8-4h10l6 2 10-5c2 0 2 2 1 3L26 34H10l-8 2"/>
  </svg>
  <h3>Many desktop publishing packages<br>and web page</h3>
  <p>It is a long established fact that a reader will be distracted by the readable content of a page when looking at its layout.</p>
</div>
<div class="abs benefit" style="left:454px;top:364px">
  <svg width="38" height="38" viewBox="0 0 38 38" fill="none" stroke="#111" stroke-width="1.3">
    <circle cx="19" cy="19" r="13"/><circle cx="19" cy="19" r="9"/>
    <path d="M19 2v4M19 32v4M2 19h4M32 19h4M7 7l3 3M28 28l3 3M31 7l-3 3M7 31l3-3"/>
    <path d="M14 23l4-4 3 2 5-6M23 15h3v3"/>
  </svg>
  <h3>There are many variations of<br>passages of Lorem Ipsum</h3>
  <p>It is a long established fact that a reader will be distracted by the readable content of a page when looking at its layout.</p>
</div>

<div class="abs band-grey"></div>
<div class="abs band-sky"></div>

<div class="abs photo" role="img" aria-label="Photo from above of a countertop POS screen and card terminal on a wooden table beside a plant"></div>
<h2 class="abs display organic-title">Creating Organic<br>Growth Requires Excellence</h2>
<p class="abs organic-copy">It is a long established fact that a reader will be distracted by the readable content of a page when looking at its layout. The point of using Lorem Ipsum is that it has a more-or-less normal distribution of letters, as opposed to using 'Content here, content here',</p>

<div class="abs hand-disc"><span role="img" aria-label="Illustration of a handshake"></span></div>
<h2 class="abs display grow-title">Grow Your Business With RBTS</h2>
<p class="abs grow-copy">If you would like to serve local businesses and help them implement software and hardware retail solutions, fill out the partnership form.</p>
<div class="abs mail">Enter Your Mail Id</div>
<div class="abs subscribe">SUBSCRIBE NEWSLETTER</div>

<h4 class="abs foot-head" style="left:40px">Features</h4>
<h4 class="abs foot-head" style="left:183px">Solutions</h4>
<h4 class="abs foot-head" style="left:360px">Products</h4>
<h4 class="abs foot-head" style="left:507px">Contact Us</h4>
<div class="abs foot-rule"></div>
<div class="abs foot-sep" style="left:140px"><i></i></div>
<div class="abs foot-sep" style="left:318px"><i></i></div>
<div class="abs foot-sep" style="left:469px"><i></i></div>

<ul class="abs foot-list" style="left:40px">
  <li>Point of Sale</li><li>Store Management</li><li>Menus &amp; Modifiers</li><li>Checkout</li><li>Customer Loyalty</li><li>Inventory</li>
</ul>
<ul class="abs foot-list" style="left:183px">
  <li>Bakery POS</li><li>Bar POS</li><li>Coffee Shop POS</li><li>Food Truck POS</li><li>Liquor Store POS</li><li>Quick Service Restaurant POS</li>
</ul>
<ul class="abs foot-list" style="left:360px">
  <li>Tillbright POS</li><li>Back Office</li><li>Dashboard</li><li>Kitchen Display</li><li>Customer Display</li><li>Employee Management</li>
</ul>

<div class="abs contact-row" style="top:1026px">
  <svg width="8" height="10" viewBox="0 0 8 10"><path d="M4 0a4 4 0 0 1 4 4c0 3-4 6-4 6S0 7 0 4a4 4 0 0 1 4-4z" fill="#111"/><circle cx="4" cy="4" r="1.5" fill="#e3f2fb"/></svg>
  <span>41 Cedar Hollow Ln, Suite 190,<br>Warren, NJ 07059</span>
</div>
<div class="abs contact-row" style="top:1060px">
  <svg width="8" height="8" viewBox="0 0 8 8"><path d="M1 0h2l1 2-1 1c.5 1 1 1.5 2 2l1-1 2 1v2c0 .6-.4 1-1 1C3 8 0 5 0 1c0-.6.4-1 1-1z" fill="#111"/></svg>
  <span>Phone: 877-555-0148</span>
</div>
<div class="abs contact-row" style="top:1083px">
  <svg width="9" height="7" viewBox="0 0 9 7"><rect width="9" height="7" fill="#111"/><path d="M0 0l4.5 4L9 0" stroke="#e3f2fb" fill="none"/></svg>
  <span>contact@rbtsmail.com</span>
</div>
<span class="abs follow">Follow :</span>
<span class="abs social" style="left:550px" role="img" aria-label="Social link"></span>
<span class="abs social" style="left:575px" role="img" aria-label="Social link"></span>
<span class="abs social" style="left:601px" role="img" aria-label="Social link"></span>
<span class="abs social" style="left:627px" role="img" aria-label="Social link"></span>

<p class="abs copyright">© 2021 <b>RBTS</b>. All Rights Reserved</p>

</body>
</html>
```